Clear Plastic Card Design

I am looking to have a business card designed from my logo icon. I am looking to match the style of a different business card I have attached in the files.
Looking for a card that is plastic, with layers of transparency in the shape of my logo icon (also attached in the files) - not a circle like the other card. The winning design will incorporate the red icon logo on the front and back and include the charity's name, "Lanterns for the Weary" in the same or similar font, as well as an email and phone number. For now, use the email: email@lanternsfortheweary.org and the phone number 555-318-4072.
We like how the sample business card has transparency, partial and full opacity layers and a matching color scheme. Files will need to be in vector so that our business card printing company can work with it.
UPDATE:
We've some excellent designs in, thank you everyone! I got an early review from the owner, and he requested a minor redirect to find his perfect design. He wants the design to stand out by NOT being a rectangle. Try instead a circle, square, or best yet - something that falls in the outline of the logo icon, either fully or partially. Thank you, everyone!
Contact Information for Business Card
Lanterns for the Weary text should be incorporated as well as a phone and email.
Look and feel

```html
<!DOCTYPE html>
<html lang="en">
<head>
<meta charset="utf-8">
<title>Lanterns for the Weary – Round Card</title>
<link rel="stylesheet" href="https://fonts.googleapis.com/css2?family=Arimo:wght@400&display=swap">
<style>
  :root {
    --page: #e2e2e2;
    --card-face: #ffffff;
    --ring-orange: #f07414;
    --ring-red: #e2301c;
    --ring-crimson: #d61b48;
    --ink: #1a1a1a;
    --brand-red: #e02a2a;
  }
  html, body {
    margin: 0;
    padding: 0;
    width: 1175px;
    height: 1200px;
    overflow: hidden;
    background: var(--page);
    font-family: "Arimo", Arial, sans-serif;
  }
  .round-card {
    position: absolute;
    left: 225px;
    top: 238px;
    width: 724px;
    height: 724px;
  }
  .round-card__ring {
    position: absolute;
    inset: 0;
    width: 724px;
    height: 724px;
  }
  .round-card__face {
    position: absolute;
    left: 60px;
    top: 60px;
    width: 604px;
    height: 604px;
    border-radius: 50%;
    background: var(--card-face);
  }
  .contact-icons {
    position: absolute;
    top: 165px;
    left: 0;
    width: 100%;
    display: flex;
    justify-content: center;
    align-items: center;
    gap: 6px;
  }
  .contact-icons__rule {
    width: 26px;
    height: 2px;
    background: var(--ink);
    margin: 0 6px;
  }
  .contact-icons svg { width: 36px; height: 36px; display: block; }
  .contact-lines {
    position: absolute;
    top: 228px;
    left: 0;
    width: 100%;
    text-align: center;
    color: var(--ink);
    font-size: 29px;
    line-height: 40px;
  }
  .contact-lines p { margin: 0; }
  .brand-name {
    position: absolute;
    left: 120px;
    top: 400px;
    display: flex;
    align-items: flex-end;
    gap: 26px;
  }
  .brand-name__text {
    font-size: 34px;
    line-height: 40px;
    color: var(--brand-red);
  }
  .brand-name__square {
    width: 120px;
    height: 120px;
    background: var(--brand-red);
  }
</style>
</head>
<body>
  <div class="round-card">
    <svg class="round-card__ring" viewBox="0 0 724 724" role="img" aria-label="Faceted orange-to-crimson polygon pattern around the card edge">
      <defs>
        <linearGradient id="ringGradient" x1="0.85" y1="0.05" x2="0.15" y2="0.95">
          <stop offset="0" stop-color="var(--ring-orange)"/>
          <stop offset="0.5" stop-color="var(--ring-red)"/>
          <stop offset="1" stop-color="var(--ring-crimson)"/>
        </linearGradient>
      </defs>
      <circle cx="362" cy="362" r="362" fill="url(#ringGradient)"/>
    </svg>

    <div class="round-card__face">
      <div class="contact-icons">
        <span class="contact-icons__rule"></span>
        <svg viewBox="0 0 36 36" aria-label="Phone">
          <circle cx="18" cy="18" r="18" fill="#111"/>
          <path d="M12 9c1-1 2-1 3 0l2 3c.6 1 .4 1.8-.4 2.4l-1 .8c.8 2 2.3 3.6 4.3 4.4l.8-1c.6-.8 1.4-1 2.4-.4l3 2c1 .7 1 1.8 0 2.8l-1.4 1.4c-1.4 1.4-4 1-7-1.2-3-2.2-5.6-5.4-6.6-8.2-.8-2.2-.6-3.8.4-4.6z" fill="#fff"/>
        </svg>
        <svg viewBox="0 0 36 36" aria-label="Email">
          <circle cx="18" cy="18" r="18" fill="#111"/>
          <rect x="8" y="11" width="20" height="14" rx="1.5" fill="#fff"/>
          <path d="M8.5 12l9.5 7.5 9.5-7.5" fill="none" stroke="#111" stroke-width="1.6"/>
        </svg>
        <svg viewBox="0 0 36 36" aria-label="Website">
          <circle cx="18" cy="18" r="18" fill="#111"/>
          <circle cx="18" cy="18" r="10" fill="#fff"/>
          <path d="M12 14c2-1 4 0 4 2s-2 2-1 4 0 4-2 3M20 10c0 2 2 3 4 2M22 20c1-1 3-1 4 1" fill="none" stroke="#111" stroke-width="2"/>
        </svg>
        <span class="contact-icons__rule"></span>
      </div>

      <div class="contact-lines">
        <p class="contact-lines__phone">555-318-4072</p>
        <p class="contact-lines__email">email@lanternsfortheweary.org</p>
        <p class="contact-lines__web">www.lanternsfortheweary.org</p>
      </div>

      <div class="brand-name">
        <span class="brand-name__text">Lanterns for the<br>Weary</span>
        <span class="brand-name__square"></span>
      </div>
    </div>
  </div>
</body>
</html>
```